Marn-ridge Tide Harbor Custom Brokers Limited

Name: Dorvella Hastings
Title: Customs Broker
Address: Shop 9 Birchfield Commercial Complex
207-209 Harlow Road
Kingston 8
Telephone: (876)
Email: tideharborport@quillmail.example

```html
<!DOCTYPE html>
<html lang="en">
<head>
<meta charset="utf-8">
<title>Marn-ridge Tide Harbor – Business Card</title>
<link rel="stylesheet" href="https://fonts.googleapis.com/css2?family=Poppins:wght@300;400;500;600;700&display=swap">
<style>
  :root {
    --navy: #14213a;
    --navy-deep: #0b1426;
    --orange: #d8861c;
    --grey: #8a8d93;
    --card-light: #f2f3f4;
    --page: #e6e4e0;
  }
  html, body {
    margin: 0;
    width: 1200px;
    height: 970px;
    overflow: hidden;
    background: var(--page);
    font-family: "Poppins", sans-serif;
  }
  .card {
    position: absolute;
    left: 60px;
    top: 178px;
    width: 1180px;
    height: 672px;
    transform: scale(0.915);
    transform-origin: top left;
    background: linear-gradient(135deg, #ffffff 0%, var(--card-light) 60%, #e9ebee 100%);
    overflow: hidden;
    box-shadow: 0 10px 30px rgba(0,0,0,0.18);
  }
  .card-shape {
    position: absolute;
    inset: 0;
  }
  .brand {
    position: absolute;
    left: 58px;
    top: 180px;
    display: flex;
    align-items: center;
    gap: 16px;
  }
  .brand-dot {
    width: 46px;
    height: 46px;
    border-radius: 50%;
    background: var(--orange);
  }
  .brand-name {
    margin: 0;
    font-size: 44px;
    font-weight: 600;
    color: var(--navy);
    letter-spacing: 0.5px;
    text-transform: uppercase;
    line-height: 1;
  }
  .tagline {
    position: absolute;
    left: 98px;
    top: 292px;
    margin: 0;
    font-size: 23px;
    font-weight: 400;
    color: var(--grey);
    letter-spacing: 8px;
  }
  .person {
    position: absolute;
    left: 58px;
    top: 358px;
  }
  .person-name {
    margin: 0;
    font-size: 36px;
    font-weight: 700;
    color: var(--navy);
    text-transform: uppercase;
    line-height: 1.15;
  }
  .person-title {
    margin: 0;
    font-size: 28px;
    font-weight: 400;
    color: var(--orange);
    line-height: 1.15;
  }
  .address {
    position: absolute;
    left: 60px;
    top: 450px;
    margin: 0;
    font-style: normal;
    font-size: 26px;
    font-weight: 400;
    color: var(--navy);
    line-height: 37px;
  }
  .contacts {
    position: absolute;
    left: 60px;
    top: 543px;
    margin: 0;
    padding: 0;
    list-style: none;
    font-size: 27px;
    color: var(--navy);
  }
  .contacts li {
    display: flex;
    align-items: center;
    gap: 16px;
    height: 41px;
  }
  .contact-icon {
    width: 32px;
    height: 32px;
    flex: none;
  }
</style>
</head>
<body>
  <div class="card">
    <svg class="card-shape" viewBox="0 0 1180 672" width="1180" height="672" aria-hidden="true">
      <path d="M740 0 L1180 0 L1180 672 L845 672 C1000 570 1075 440 1066 350 C1055 210 930 85 740 0 Z" fill="var(--navy-deep)"/>
      <path d="M430 0 C760 60 1035 220 1050 390 C1060 500 990 600 860 672" fill="none" stroke="var(--orange)" stroke-width="8"/>
    </svg>

    <div class="brand">
      <span class="brand-dot"></span>
      <p class="brand-name">Marn-ridge Tide Harbor</p>
    </div>
    <p class="tagline">Custom Brokers Ltd.</p>

    <div class="person">
      <p class="person-name">Dorvella Hastings</p>
      <p class="person-title">Customs Broker</p>
    </div>

    <address class="address">
      Shop 9 Birchfield Commercial Complex<br>
      207-209 Harlow Road, Kingston 8
    </address>

    <ul class="contacts">
      <li>
        <svg class="contact-icon" viewBox="0 0 32 32" aria-hidden="true">
          <circle cx="16" cy="16" r="15" fill="var(--orange)"/>
          <rect x="11" y="8" width="10" height="16" rx="2" fill="none" stroke="#fff" stroke-width="2"/>
          <line x1="14" y1="21" x2="18" y2="21" stroke="#fff" stroke-width="1.5"/>
        </svg>
        <span>(876) 555 014 2270</span>
      </li>
      <li>
        <svg class="contact-icon" viewBox="0 0 32 32" aria-hidden="true">
          <circle cx="16" cy="16" r="15" fill="var(--orange)"/>
          <rect x="8" y="10" width="16" height="12" rx="1.5" fill="none" stroke="#fff" stroke-width="2"/>
          <polyline points="8.5,11 16,17 23.5,11" fill="none" stroke="#fff" stroke-width="2"/>
        </svg>
        <span>tideharborport@quillmail.example</span>
      </li>
    </ul>
  </div>
</body>
</html>
```